Business Card for TOV

We need a Corporate style business card for a new Industrial recycling company based in Australia. We recycle industrial products from Mining companies, power stations and other large industry all around the country.

We want the card to represent a modern, innovative professional company that is an industry leader.

We want the card to be double sided. I think with the logo centred by itself on one side and the text displayed with all our details on the other side.

(or you could put the persons name with the job title on the side with the logo?? I'll leave that up to your creative sides)

Open to how you divide and place the information on the one side of the card.

I think the persons name and the title should have its own place. The rest of the information can be placed as you think is best and then I will provide feedback as to what I think works best.

I have attached the logo file so you can add that to the one side. Whether you use it in a smaller form on the second side too is an option but I'll leave that up to you initially?

Information required on the card is as follows

Dermot Halloran
Director

0438 972 506

dermot@tovq.com.au

Po Box 782
Brindle ACT 2694

www.tovq.com.au

ACN 582 917 306 (This can be in very small print and can be in the bottom corner of the card or somewhere not very prominent

Wanted to thank everyone for their submissions. 

We were really torn on about 5 designs in the end.

We decided to go with the first one we liked.

We have another company that is going to need logo and business card design in the coming weeks.

I will save your designer ID's so I can invite you all to that project. too!

Thanks again and all the best

Dermot

Target Market(s)

Corporate and medium to large business clients

Industry/Entity Type

Industrial

```html
<!DOCTYPE html>
<html lang="en">
<head>
<meta charset="utf-8">
<title>TOV Business Card</title>
<link rel="stylesheet" href="https://fonts.googleapis.com/css2?family=Nunito+Sans:wght@300;400;600;800&display=swap">
<style>
  :root {
    --bg: #e4e6e8;
    --card: #ffffff;
    --green: #8cd233;
    --blue: #3aaeea;
    --ink: #2a2a2a;
    --muted: #555;
  }
  * { box-sizing: border-box; margin: 0; padding: 0; }
  html, body { width: 1200px; height: 800px; overflow: hidden; }
  body {
    background: var(--bg);
    font-family: "Nunito Sans", Arial, sans-serif;
    color: var(--ink);
    display: flex;
    align-items: center;
    justify-content: center;
    gap: 40px;
  }
  .card {
    position: relative;
    width: 540px;
    height: 309px;
    background: var(--card);
    box-shadow: 0 10px 30px rgba(0,0,0,0.12);
    overflow: hidden;
  }

  /* Brand mark: plain circle plus name */
  .brand { display: flex; align-items: center; gap: 10px; }
  .brand-dot { width: 34px; height: 34px; border-radius: 50%; background: var(--green); flex: none; }
  .brand-name {
    font-weight: 800;
    color: var(--ink);
    text-transform: uppercase;
    line-height: 1.05;
    font-size: 15px;
    letter-spacing: 0.5px;
  }

  /* Logo side */
  .card-logo {
    border-top: 5px solid var(--blue);
    border-right: 5px solid var(--blue);
    border-bottom: 5px solid var(--green);
    border-left: 5px solid var(--green);
  }
  .card-logo .tab-green {
    position: absolute; left: 0; top: 90px;
    width: 80px; height: 58px;
    background: var(--green);
    clip-path: polygon(0 0, 100% 0, 82% 100%, 0 100%);
  }
  .card-logo .tab-blue {
    position: absolute; right: 0; bottom: 40px;
    width: 80px; height: 58px;
    background: var(--blue);
    clip-path: polygon(18% 0, 100% 0, 100% 100%, 0 100%);
  }
  .card-logo .brand {
    position: absolute; left: 50%; top: 50%;
    transform: translate(-50%, -50%);
  }
  .card-logo .brand-dot { width: 54px; height: 54px; }
  .card-logo .brand-name { font-size: 22px; }

  /* Details side */
  .card-details .brand { position: absolute; right: 28px; top: 34px; }
  .name-band {
    position: absolute; left: 0; top: 96px;
    width: 330px; height: 46px;
    background: var(--green);
    display: flex; align-items: center;
    padding-left: 40px;
  }
  .person-name { color: #fff; font-weight: 400; font-size: 26px; letter-spacing: 0.5px; }
  .title-band {
    position: absolute; right: 0; top: 142px;
    width: 198px; height: 40px;
    background: var(--blue);
    display: flex; align-items: center; justify-content: flex-end;
    padding-right: 26px;
  }
  .person-title { color: #fff; font-weight: 300; font-size: 21px; }
  .address {
    position: absolute; left: 40px; top: 158px;
    font-size: 15px; line-height: 1.35; font-style: normal; color: var(--ink);
  }
  .company-number {
    position: absolute; left: 40px; top: 238px;
    font-size: 9px; color: var(--muted); letter-spacing: 0.3px;
  }
  .contacts {
    position: absolute; left: 316px; top: 198px;
    list-style: none;
    font-size: 14.5px; line-height: 1;
  }
  .contacts li { display: flex; align-items: center; gap: 12px; height: 28px; }
  .contacts svg { width: 16px; height: 16px; flex: none; }
</style>
</head>
<body>

  <section class="card card-logo" aria-label="Card back">
    <div class="tab-green"></div>
    <div class="tab-blue"></div>
    <div class="brand">
      <span class="brand-dot"></span>
      <span class="brand-name">Tovara<br>Industrial Recovery</span>
    </div>
  </section>

  <section class="card card-details" aria-label="Card front">
    <div class="brand">
      <span class="brand-dot"></span>
      <span class="brand-name">Tovara<br>Industrial Recovery</span>
    </div>

    <div class="name-band"><h1 class="person-name">Dermot Halloran</h1></div>
    <div class="title-band"><p class="person-title">Director</p></div>

    <address class="address">Po Box 782<br>Brindle ACT 2694</address>
    <p class="company-number">ACN 582 917 306</p>

    <ul class="contacts">
      <li>
        <svg viewBox="0 0 16 16" aria-hidden="true"><path fill="#3aaeea" d="M3 2h3l1 3-2 1.2a8 8 0 0 0 4.8 4.8L11 9l3 1v3a1 1 0 0 1-1 1A12 12 0 0 1 2 3a1 1 0 0 1 1-1z"/></svg>
        0438 972 506
      </li>
      <li>
        <svg viewBox="0 0 16 16" aria-hidden="true"><rect x="1.5" y="3.5" width="13" height="9" fill="none" stroke="#3aaeea" stroke-width="1.2"/><path d="M1.5 3.5 8 9l6.5-5.5" fill="none" stroke="#3aaeea" stroke-width="1.2"/></svg>
        dermot@tovq.com.au
      </li>
      <li>
        <svg viewBox="0 0 16 16" aria-hidden="true"><g fill="none" stroke="#3aaeea" stroke-width="1.1"><circle cx="8" cy="8" r="6.5"/><ellipse cx="8" cy="8" rx="3" ry="6.5"/><path d="M1.5 8h13M2.5 4.8h11M2.5 11.2h11"/></g></svg>
        www.tovq.com.au
      </li>
    </ul>
  </section>

</body>
</html>
```